Electrical Busness

We require an a5 flyer that promotes our Electrical business. Things we would like included are;
1) our business name, Brightpath Electrical and Communication
2) Our Electrical license, EC 62073
3) Our ABN, 37 512 906 284
4) Our website, www.ozwirespark.com.au
5) Our Email, info@ozwirespark.com.au
6) Our contact number, 0412 586 027
8) Our logo, I will attach this (can you please change it so the bbackground is white not black)
9) Our colours are red and white and some black
10) 'over 8 years experience'
11) 'call today for a free quote'
12) 'friendly, honest and reliable workmanship'
13) 'local Electrician in your area'
14)' servicing Cannington, Melville, Manning, Thornlie, Victoria Park, Canning Vale, Forrestfeild and many more'
15) 'Renovations, additions, upgrades, new installations, maintenance'
16) 'available 24/7 for emergency call outs'
17) 'LED downlights, smoke alarms, RCDs, smoke detectors, power & USB points, dimmers, data, phone points, switchboard upgrade, security lighting, safety certificate, compliance and safety checks, exit and emergency lighting and many more'
18) 'WA qualified and fully insured'
19) 'GTRO member' (will attach logo)

```html
<!DOCTYPE html>
<html lang="en">
<head>
<meta charset="utf-8">
<title>Brightpath Electrical and Communication – A5 Flyer</title>
<link rel="stylesheet" href="https://fonts.googleapis.com/css2?family=Oswald:wght@500;600&family=Open+Sans:ital,wght@0,400;0,600;1,400&display=swap">
<style>
  :root {
    --red: #e51d24;
    --red-bright: #f2262c;
    --black: #1c1c1c;
    --charcoal: #3a3a3a;
    --grey-light: #f1f1f1;
    --white: #ffffff;
    --text: #222222;
    --badge-blue: #1f5aa6;
  }
  * { margin: 0; padding: 0; box-sizing: border-box; }
  html, body { width: 1200px; height: 1200px; overflow: hidden; }
  body {
    background: linear-gradient(180deg, #ececec 0%, #d9d9d9 100%);
    font-family: "Open Sans", Arial, sans-serif;
    color: var(--text);
  }
  .flyer {
    position: absolute;
    left: 204px; top: 40px;
    width: 792px; height: 1120px;
    background: var(--white);
    overflow: hidden;
    box-shadow: 0 10px 30px rgba(0,0,0,.18);
  }
  .flyer-shapes { position: absolute; inset: 0; }
  .heading { font-family: "Oswald", Arial, sans-serif; font-weight: 600; text-transform: uppercase; line-height: 1; }

  .photo-area {
    position: absolute; left: 190px; top: 70px; width: 602px; height: 425px;
    clip-path: polygon(0 0, 100% 0, 100% 100%, 75% 94%, 0 94%);
  }

  .brand-mark {
    position: absolute; left: 40px; top: 118px;
    display: flex; align-items: center; gap: 12px;
    font-family: "Oswald", Arial, sans-serif; font-weight: 600;
    font-size: 34px; color: var(--red); line-height: 1;
  }
  .brand-mark .dot { width: 22px; height: 22px; border-radius: 50%; background: var(--red); }

  .get-in-touch {
    position: absolute; left: 22px; top: 330px; width: 160px;
    text-align: center; color: var(--white); font-size: 40px; transform: rotate(8deg);
  }
  .get-in-touch .accent { color: var(--red-bright); font-size: 30px; display: block; margin-top: 4px; }

  .experience {
    position: absolute; left: 34px; top: 548px; width: 410px;
    font-size: 30px; color: var(--black); white-space: nowrap;
  }
  .experience .big { color: var(--red); font-size: 44px; }

  .key-points { position: absolute; left: 36px; top: 610px; list-style: none; font-size: 17px; line-height: 1.45; }
  .key-points li { position: relative; padding-left: 22px; }
  .key-points li::before {
    content: ""; position: absolute; left: 0; top: 7px;
    width: 12px; height: 12px; border-radius: 50%; background: var(--red);
  }

  .services-detail {
    position: absolute; left: 36px; top: 745px; width: 390px;
    font-size: 13.5px; font-style: italic; line-height: 1.4; text-align: justify; color: #333;
  }
  .service-area {
    position: absolute; left: 36px; top: 855px; width: 390px;
    font-size: 13.5px; font-style: italic; line-height: 1.4; color: #333;
  }

  .credentials {
    position: absolute; left: 28px; top: 930px; width: 390px; height: 38px;
    border-radius: 19px; background: linear-gradient(180deg, #555, #1f1f1f);
    color: var(--white); font-size: 13px; font-weight: 600;
    display: flex; align-items: center; justify-content: center;
  }

  .contact-web {
    position: absolute; left: 28px; top: 1040px;
    color: var(--white); font-size: 13px; white-space: nowrap;
  }

  .business-name { position: absolute; left: 480px; top: 545px; width: 290px; color: var(--white); }
  .business-name .name { font-size: 46px; display: block; }
  .business-name .tagline { font-size: 19px; font-weight: 500; display: block; margin-top: 4px; }

  .service-types { position: absolute; left: 490px; top: 640px; list-style: none; color: var(--white); font-size: 19px; font-weight: 600; line-height: 1.3; }
  .service-types li { position: relative; padding-left: 20px; }
  .service-types li::before {
    content: ""; position: absolute; left: 0; top: 9px;
    width: 9px; height: 9px; border-radius: 50%; background: var(--black);
  }

  .call-to-action {
    position: absolute; left: 482px; top: 840px; width: 278px; height: 132px;
    border-radius: 26px; background: linear-gradient(180deg, #4a4a4a, #111);
    color: var(--white); text-align: center; padding-top: 16px;
  }
  .call-to-action .line { font-size: 30px; display: block; }
  .call-to-action .accent { color: var(--red-bright); }
  .call-to-action .phone { font-size: 38px; display: block; margin-top: 4px; }

  .member-badge {
    position: absolute; left: 580px; top: 1018px;
    display: flex; align-items: center; gap: 12px;
  }
  .member-badge .badge { width: 58px; height: 34px; background: var(--badge-blue); border-radius: 4px; }
  .member-badge .label { font-size: 16px; font-weight: 600; color: var(--badge-blue); }
</style>
</head>
<body>
  <article class="flyer">
    <svg class="flyer-shapes" viewBox="0 0 792 1120" width="792" height="1120" aria-hidden="true">
      <defs>
        <linearGradient id="midGrey" x1="0" y1="0" x2="0" y2="1">
          <stop offset="0" stop-color="#ffffff"/>
          <stop offset="1" stop-color="#e9e9e9"/>
        </linearGradient>
        <linearGradient id="darkPanel" x1="0" y1="0" x2="1" y2="1">
          <stop offset="0" stop-color="#5a5a5a"/>
          <stop offset="1" stop-color="#1e1e1e"/>
        </linearGradient>
        <linearGradient id="bottomDark" x1="0" y1="0" x2="0" y2="1">
          <stop offset="0" stop-color="#4a4a4a"/>
          <stop offset="1" stop-color="#1a1a1a"/>
        </linearGradient>
      </defs>
      <rect width="792" height="1120" fill="url(#midGrey)"/>
      <polygon points="190,70 792,70 792,495 640,470 190,470" fill="#8a8f96"/>
      <polygon points="0,0 392,0 392,62 225,300 0,190" fill="#f4f4f4"/>
      <polyline points="392,62 225,300 0,190" fill="none" stroke="var(--red)" stroke-width="9"/>
      <polygon points="0,205 200,300 210,470 0,485" fill="url(#darkPanel)"/>
      <polyline points="200,300 210,470" stroke="var(--red)" stroke-width="6" fill="none"/>
      <polygon points="0,480 620,468 792,505 792,515 620,478 0,492" fill="var(--red)"/>
      <polygon points="455,532 792,498 792,1000 455,1000" fill="var(--red)"/>
      <polygon points="0,985 460,985 540,1120 0,1120" fill="var(--red)"/>
      <polygon points="513,1075 792,1075 792,1120 540,1120" fill="url(#bottomDark)"/>
    </svg>

    <div class="photo-area" role="img" aria-label="Photo of an electrician in a hard hat working on a switchboard"></div>

    <div class="brand-mark"><span class="dot"></span>Brightpath</div>

    <p class="get-in-touch heading">Get in touch <span class="accent">with us!</span></p>

    <h2 class="experience heading">Over <span class="big">8 years</span> experience</h2>

    <ul class="key-points">
      <li>Friendly, honest and reliable workmanship</li>
      <li>Available 24/7 for emergency call outs</li>
      <li>Local Electrician in your area</li>
      <li>WA qualified and fully insured</li>
    </ul>

    <p class="services-detail">LED downlights, smoke alarms, RCDs, smoke detectors, power &amp; USB points, dimmers, data, phone points, switchboard upgrade, security lighting, safety certificate, compliance and safety checks, exit and emergency lighting and many more.</p>

    <p class="service-area">Servicing Cannington, Melville, Manning, Thornlie, Victoria Park, Canning Vale, Forrestfeild and many more.</p>

    <p class="credentials">Our Electrical license, EC 62073 &nbsp;|&nbsp; Our ABN, 37 512 906 284</p>

    <p class="contact-web">Visit: www.ozwirespark.com.au | Email, info@ozwirespark.com.au</p>

    <h1 class="business-name heading">
      <span class="name">Brightpath</span>
      <span class="tagline">Electrical &amp; Communication</span>
    </h1>

    <ul class="service-types">
      <li>Renovations</li>
      <li>Additions</li>
      <li>Upgrades</li>
      <li>New installations</li>
      <li>Maintenance</li>
    </ul>

    <div class="call-to-action heading">
      <span class="line">Call today for</span>
      <span class="line accent">a free quote</span>
      <span class="phone">0412 586 027</span>
    </div>

    <div class="member-badge">
      <span class="badge" aria-hidden="true"></span>
      <span class="label">GTRO</span>
    </div>
  </article>
</body>
</html>
```